Cobalt Press website re-design

We would like to recreate the www.cobaltpress-demo.com.au website into a simpler and more sophisticated version. We want the buyer to be drawn to our site and establish that we are reputable and professional from the moment they enter. We want them to easily find the product or service they are looking for within our site, decide that they would like to find out more and either click through to obtain a quote or click through to contact a rep.

The current website has been created using MS Front Page, however we would like the newly designed site to be created in a mobile responsive WordPress CMS format

We are a Print Broker who can save clients time in hunting around for the right supplier for their print jobs. This is most likely appealing to larger organisations who haven’t got time to waste in finding quotes from many different suppliers for each type of job. We make it easy because we have access to a large network of trade only print & signage suppliers so we can select the best and most cost effective supplier depending on the type of print job. Further, because we don’t do the printing in-house we have low overheads which means we can ensure competitive prices.
Updates

Target Market(s)

Business owners, print managers, receptionists, marketing managers who are time poor, uneducated re:printing, after quick & cost effective solutions

Industry/Entity Type

Printing

Requirements
Must have
• Use the current logo and colours - see files uploaded
Limit scrolling and keep pages within view
Easy to see buttons that navigate the buyer through the site
The site is to be clear, easy to understand, free from clutter (ie.ensure white space) and have a Professional/corporate look
Easy to use Quotation forms
Imagery needs to be modern, and clean -see brightmarrow site

Competitor/other websites we like and why?
I like brightmarrow.com.au for its’ modern look. I like how the products are displayed in High resolution are very clean and uncluttered. You can easily find the product and access ‘get a quote’.
Pelham Print has a good layout for the quote request. Check out pelhamprint-demo.com.au
www.vendrak.com.au are print brokers/managers. Their descriptions are easy to understand but still heavy in content.
Nice to have
• 1. Home Page
½ page summary of the core business
Distinct buttons for products and services down the side (so that people can go straight to what they need.)
About Us (including profiles); Products and Services; Get a Quote; Contact us across the top

2. About Us
A brief overview of owner, staff and reps. Click through to Profiles for each region rep and contact details either as pop ups or separate pages.

3. Products and Services
Buttons or lists of products link to pop up with get a quote link within (this could be grouped such as Business Cards, Letterheads, Folders etc.; Club printing with plastic cards, sign in books, coasters etc.; Marketing such as flyers, posters, banners etc. (Note. look at how others have broken it up)
Include calling for advice for special products and finishes as service on how a job can be improved and done within budget.
4. Get a Quote
(2 sites mentioned below that I like for the get a quote system)

5. Contact Us
Clear sections divided by lines and details large starting with 1300 number
Head office
Regional numbers and areas they cover
Include emails.

Contact us now or click to request a rep contact you.

```html
<!DOCTYPE html>
<html lang="en">
<head>
<meta charset="utf-8">
<title>Cobalt Press — Home</title>
<link rel="stylesheet" href="https://fonts.googleapis.com/css2?family=PT+Sans:ital,wght@0,400;0,700;1,400&display=swap">
<style>
  :root {
    --red: #b3172d;
    --red-dark: #8e1424;
    --charcoal: #2b2b2b;
    --hero-bg: #f5f5f5;
    --band: #e0e0e0;
    --text: #333333;
    --muted: #666666;
    --white: #ffffff;
    --nav-text: #e6e6e6;
  }
  * { box-sizing: border-box; margin: 0; padding: 0; }
  html, body { width: 1200px; height: 926px; overflow: hidden; }
  body {
    position: relative;
    font-family: "PT Sans", Arial, sans-serif;
    color: var(--text);
    background: var(--white);
  }

  /* Header */
  .site-header { position: absolute; left: 0; top: 0; width: 1200px; height: 87px; background: var(--charcoal); }
  .brand {
    position: absolute; left: 173px; top: 30px;
    display: flex; align-items: center; gap: 8px;
    color: var(--white); font-size: 18px; font-weight: 700; letter-spacing: 0.5px;
  }
  .brand-mark { width: 22px; height: 22px; background: var(--red); border-radius: 4px; }
  .main-nav { position: absolute; left: 338px; top: 37px; display: flex; gap: 0; }
  .main-nav a {
    color: var(--nav-text); text-decoration: none;
    font-size: 10px; letter-spacing: 1.6px; text-transform: uppercase;
    margin-right: 27px;
  }
  .main-nav a.is-active { color: #d9364a; }
  .main-nav a:last-child { margin-right: 0; }

  /* Hero */
  .hero { position: absolute; left: 0; top: 87px; width: 1200px; height: 249px; background: var(--hero-bg); }
  .hero-photo {
    position: absolute; left: 240px; top: 14px; width: 278px; height: 235px;
    background: linear-gradient(180deg, #d9cfc8 0%, #c9a89a 35%, #a62233 60%, #8e1424 100%);
    border-radius: 120px 120px 0 0;
  }
  .hero-title {
    position: absolute; left: 683px; top: 40px;
    font-size: 26px; font-weight: 400; line-height: 28px; letter-spacing: 2.4px; color: var(--red);
  }
  .hero-quote {
    position: absolute; left: 683px; top: 110px; width: 380px;
    font-size: 13px; font-style: italic; line-height: 21px; letter-spacing: 0.5px; color: #333;
  }
  .btn {
    position: absolute; display: flex; align-items: center; justify-content: center; gap: 6px;
    background: linear-gradient(180deg, #c8243a 0%, #a3142a 100%);
    border: 1px solid #7c0f1e; border-radius: 3px;
    color: var(--white); font-weight: 700; font-size: 11px; letter-spacing: 0.7px; text-decoration: none;
    box-shadow: inset 0 1px 0 rgba(255,255,255,0.25);
  }
  .btn-quote { left: 682px; top: 165px; width: 215px; height: 35px; text-transform: uppercase; }

  /* Product band */
  .hero-rule { position: absolute; left: 0; top: 336px; width: 1200px; height: 4px; background: var(--red); }
  .product-band { position: absolute; left: 0; top: 340px; width: 1200px; height: 97px; background: var(--band); }
  .product-col { position: absolute; top: 13px; list-style: none; }
  .product-col li {
    display: flex; align-items: center; gap: 5px; height: 19px;
    font-size: 9.5px; letter-spacing: 1.2px; text-transform: uppercase; color: #333;
  }
  .product-col svg { width: 13px; height: 12px; flex: none; }

  /* Intro */
  .intro {
    position: absolute; left: 173px; top: 458px; width: 615px;
    font-size: 13.2px; font-style: italic; line-height: 27.5px; letter-spacing: 0.6px; color: #333;
  }
  .btn-call { left: 857px; top: 478px; width: 171px; height: 35px; font-size: 11.5px; }

  /* Feature columns */
  .feature { position: absolute; top: 574px; width: 190px; text-align: center; }
  .feature-art { width: 96px; height: 100px; margin: 0 auto; border-radius: 50%; }
  .feature-shadow { width: 130px; height: 10px; margin: 4px auto 11px; border-radius: 50%;
    background: radial-gradient(ellipse at center, rgba(0,0,0,0.25) 0%, rgba(0,0,0,0) 70%); }
  .feature-label {
    width: 165px; height: 22px; margin: 0 auto; line-height: 22px;
    background: var(--red-dark); color: var(--white);
    font-size: 10px; font-weight: 700; letter-spacing: 0.8px; text-transform: uppercase;
  }
  .feature-text { margin-top: 8px; font-size: 10.5px; line-height: 19px; letter-spacing: 0.8px; color: var(--muted); }
  .feature-more { display: block; margin-top: 7px; font-size: 10px; font-weight: 700; letter-spacing: 0.8px; color: #222; text-decoration: none; }
  .art-person { background: radial-gradient(circle at 50% 40%, #8a8a8a 0%, #3a3a3a 70%); border-radius: 45% 45% 20% 20%; }
  .art-screen { background: linear-gradient(160deg, #5a5a5a 0%, #111 70%); border-radius: 6px; height: 80px; margin-top: 10px; width: 104px; }
  .art-document { background: linear-gradient(180deg, #f4f4f4 0%, #cfcfcf 100%); border-radius: 3px; width: 70px; }
  .art-globe { background: radial-gradient(circle at 35% 35%, #e6e6e6 0%, #9a9a9a 55%, #555 100%); width: 92px; height: 92px; }

  /* Footer */
  .site-footer { position: absolute; left: 0; top: 861px; width: 1200px; height: 65px; background: #2d2d2d; }
  .copyright { position: absolute; left: 180px; top: 24px; font-size: 10.5px; letter-spacing: 0.8px; color: #c8c8c8; }
  .copyright span { color: #d9364a; }
  .social { position: absolute; left: 532px; top: 20px; display: flex; gap: 15px; }
  .social i { width: 22px; height: 22px; border-radius: 50%; display: block; }
  .social .s1 { background: #1f4f7d; }
  .social .s2 { background: #2a8ed0; }
  .social .s3 { background: #e8612c; }
  .social .s4 { background: #a8a8a8; }
  .footer-nav { position: absolute; left: 810px; top: 24px; display: flex; gap: 21px; }
  .footer-nav a { font-size: 10.5px; letter-spacing: 0.8px; color: #c8c8c8; text-decoration: none; }
  .footer-nav a.is-active { color: #d9364a; }
</style>
</head>
<body>

<header class="site-header">
  <div class="brand"><span class="brand-mark"></span>Cobalt Press</div>
  <nav class="main-nav">
    <a class="is-active" href="#">Home</a>
    <a href="#">About Us</a>
    <a href="#">Products</a>
    <a href="#">Plastic Cards</a>
    <a href="#">Signage</a>
    <a href="#">Request a Quote</a>
    <a href="#">Contact Us</a>
    <a href="#">Blog</a>
  </nav>
</header>

<section class="hero">
  <div class="hero-photo" role="img" aria-label="Portrait of the owner wearing a red company polo shirt"></div>
  <h1 class="hero-title">Save time &amp; money<br>on your printing costs</h1>
  <p class="hero-quote">“Cobalt Press delivers great quality, excellent value and consistent service, every time. That’s our guarantee!”</p>
  <a class="btn btn-quote" href="#">Receive a free quote now
    <svg width="6" height="8" viewBox="0 0 6 8"><path d="M0 0 L6 4 L0 8 Z" fill="#fff"/></svg>
  </a>
</section>

<div class="hero-rule"></div>

<section class="product-band">
  <svg width="0" height="0" style="position:absolute">
    <symbol id="tick" viewBox="0 0 13 12">
      <rect x="0" y="1" width="11" height="11" rx="2" fill="#fff"/>
      <path d="M2 6 L5 9 L12 1" stroke="#c41a30" stroke-width="2.4" fill="none" stroke-linecap="round" stroke-linejoin="round"/>
    </symbol>
  </svg>
  <ul class="product-col" style="left:173px">
    <li><svg><use href="#tick"/></svg>Beer coasters</li>
    <li><svg><use href="#tick"/></svg>Brochures/flyers</li>
    <li><svg><use href="#tick"/></svg>Business cards</li>
    <li><svg><use href="#tick"/></svg>Club printing</li>
  </ul>
  <ul class="product-col" style="left:318px">
    <li><svg><use href="#tick"/></svg>Carbonless books/receipt books</li>
    <li><svg><use href="#tick"/></svg>Direct mailings/letterbox drops</li>
    <li><svg><use href="#tick"/></svg>Envelopes</li>
    <li><svg><use href="#tick"/></svg>Fridge magnets</li>
  </ul>
  <ul class="product-col" style="left:554px">
    <li><svg><use href="#tick"/></svg>Invoice books</li>
    <li><svg><use href="#tick"/></svg>Triplicate books &amp; pads)</li>
    <li><svg><use href="#tick"/></svg>Letterhead &amp; comp slips</li>
    <li><svg><use href="#tick"/></svg>Note pads</li>
  </ul>
  <ul class="product-col" style="left:739px">
    <li><svg><use href="#tick"/></svg>Loyalty cards (paper)</li>
    <li><svg><use href="#tick"/></svg>Magazines/brochures</li>
    <li><svg><use href="#tick"/></svg>Posters (any size)</li>
    <li><svg><use href="#tick"/></svg>Presentation folders</li>
  </ul>
  <ul class="product-col" style="left:907px">
    <li><svg><use href="#tick"/></svg>Post cards</li>
    <li><svg><use href="#tick"/></svg>Product boxes</li>
    <li><svg><use href="#tick"/></svg>School yearbooks</li>
    <li><svg><use href="#tick"/></svg>Stickers</li>
  </ul>
</section>

<p class="intro">Using Australia's leading print trade suppliers, we provide our clients with the most cost effec-tive print solution in the market. We are constantly sourcing the most advanced technology in the industry to produce the lowest unit price, best quality and fastest Australia wide delivery.</p>
<a class="btn btn-call" href="#">Call 1300 555 019</a>

<section class="feature" style="left:160px">
  <div class="feature-art art-person" role="img" aria-label="Dark grey figure icon representing the team"></div>
  <div class="feature-shadow"></div>
  <div class="feature-label">About Us</div>
  <p class="feature-text">Vitae pulvinar tellus sollicitudin ultrices. Morbi cursus, dolor in bibendum laoreet, libero mauri</p>
  <a class="feature-more" href="#">read more</a>
</section>

<section class="feature" style="left:390px">
  <div class="feature-art art-screen" role="img" aria-label="Computer monitor with a magnifying glass"></div>
  <div class="feature-shadow" style="margin-top:14px"></div>
  <div class="feature-label">Products &amp; Services</div>
  <p class="feature-text">Vitae pulvinar tellus sollicitudin ultrices. Morbi cursus, dolor in bibendum laoreet, libero mauri</p>
  <a class="feature-more" href="#">read more</a>
</section>

<section class="feature" style="left:622px">
  <div class="feature-art art-document" role="img" aria-label="Printed document with a pen"></div>
  <div class="feature-shadow"></div>
  <div class="feature-label">Get a Quote</div>
  <p class="feature-text">Vitae pulvinar tellus sollicitudin ultrices. Morbi cursus, dolor in bibendum laoreet, libero mauri</p>
  <a class="feature-more" href="#">read more</a>
</section>

<section class="feature" style="left:848px">
  <div class="feature-art art-globe" role="img" aria-label="Silver globe"></div>
  <div class="feature-shadow" style="margin-top:12px"></div>
  <div class="feature-label">Contact Us</div>
  <p class="feature-text">Vitae pulvinar tellus sollicitudin ultrices. Morbi cursus, dolor in bibendum laoreet, libero mauri</p>
  <a class="feature-more" href="#">read more</a>
</section>

<footer class="site-footer">
  <p class="copyright">© 2013 <span>business name</span> &nbsp;|&nbsp; All rights reserved</p>
  <div class="social"><i class="s1"></i><i class="s2"></i><i class="s3"></i><i class="s4"></i></div>
  <nav class="footer-nav">
    <a class="is-active" href="#">Home</a>
    <a href="#">Lorem</a>
    <a href="#">Ipsume</a>
    <a href="#">Contact</a>
  </nav>
</footer>

</body>
</html>
```